Custom Truck shop New Business Card design

double sided business card including my new logo, brand colors and picking a font I attached, clean and modern look. I attached the old card for some reference. and would like to include the picture of the white truck attached. I would also like to have it with one of my employees info as well. (same info except name and title Brin Tolvay Service Writer)

Dale Porvick
Owner

address
48310 E Calloway Ridge Rd S
STE 217
Marsh Hollow, CO 80219

phone 720-555-0184

email dale@brokenspurrigs.example

website brokenspurrgis.example

social @brokenspurrigs

Target Market(s)

men 18-60

Industry/Entity Type

Automotive

Contact Information for Business Card

Dale Porvick Owner address 48310 E Calloway Ridge Rd S STE 217 Marsh Hollow, CO 80219 phone 720-555-0184 email dale@brokenspurrigs.example website brokenspurrgis.example social @brokenspurrigs

Font styles to use
Other font styles liked:
• fonts attached

Requirements
Must have
• new logo, orange #FC68D, Charcoal #333333
Nice to have
• the white truck

```html
<!DOCTYPE html>
<html lang="en">
<head>
<meta charset="utf-8">
<title>Broken Spur Rigs — Business Card</title>
<link href="https://fonts.googleapis.com/css2?family=Montserrat:ital,wght@0,400;0,500;0,600;0,800;1,900&display=swap" rel="stylesheet">
<style>
  :root {
    --orange: #f26522;
    --charcoal: #333333;
    --charcoal-deep: #2a2a2a;
    --ink: #1c1c1c;
    --paper: #f4f4f3;
    --backdrop: #9c9c9c;
    --muted: #6f6f6f;
  }
  * { box-sizing: border-box; margin: 0; padding: 0; }
  html, body { width: 1200px; height: 801px; overflow: hidden; }
  body {
    background: var(--backdrop);
    font-family: "Montserrat", Arial, sans-serif;
    display: flex;
    align-items: center;
    justify-content: center;
    gap: 40px;
  }
  .card {
    position: relative;
    width: 540px;
    height: 309px;
    overflow: hidden;
    border-bottom: 4px solid var(--orange);
    box-shadow: 0 10px 24px rgba(0,0,0,.25);
  }

  /* Front */
  .card--front { background: var(--paper); }
  .truck-photo {
    position: absolute; inset: 0;
    background:
      radial-gradient(ellipse at 50% 62%, rgba(200,200,198,.9) 0%, rgba(225,225,223,.6) 45%, rgba(244,244,243,0) 75%),
      linear-gradient(180deg, #e4e6e3 0%, #eeeeed 40%, #e2e2e0 100%);
  }
  .contact-name {
    position: absolute; left: 34px; top: 26px;
    font-size: 27px; font-weight: 900; font-style: italic;
    color: var(--ink); letter-spacing: .3px;
  }
  .contact-title {
    position: absolute; left: 34px; top: 60px;
    font-size: 12.5px; font-weight: 500; color: var(--orange);
  }
  .front-brand {
    position: absolute; right: 28px; top: 80px;
    display: flex; align-items: center; gap: 8px;
  }
  .brand-dot {
    width: 22px; height: 22px; border-radius: 50%;
    background: var(--charcoal);
  }
  .brand-name {
    font-size: 14px; font-weight: 800; color: var(--charcoal);
    letter-spacing: .5px;
  }
  .address {
    position: absolute; left: 34px; top: 182px;
    font-size: 12px; font-weight: 500; line-height: 1.55;
    color: var(--ink); list-style: none;
  }
  .contact-lines {
    position: absolute; right: 26px; bottom: 22px;
    list-style: none; text-align: right;
    font-size: 12px; font-weight: 500; line-height: 1.6; color: var(--ink);
  }
  .contact-lines li { display: flex; align-items: center; justify-content: flex-end; gap: 7px; }
  .contact-lines .phone { letter-spacing: 2.5px; font-size: 13px; }
  .contact-lines svg { width: 11px; height: 11px; flex: none; }

  /* Back */
  .card--back {
    background: var(--charcoal);
    display: flex; flex-direction: column; align-items: center; justify-content: center;
    gap: 18px;
  }
  .back-circle {
    width: 88px; height: 88px; border-radius: 50%;
    background: var(--charcoal-deep);
    border: 3px solid var(--orange);
  }
  .back-name {
    font-size: 34px; font-weight: 800; color: #1f1f1f;
    letter-spacing: 1px; text-transform: uppercase;
  }
</style>
</head>
<body>

  <section class="card card--front">
    <div class="truck-photo" role="img" aria-label="Faded photo of a lifted white pickup truck parked in a lot with bare trees behind"></div>
    <h1 class="contact-name">Dale Porvick</h1>
    <p class="contact-title">CEO/Founder</p>
    <div class="front-brand">
      <span class="brand-dot"></span>
      <span class="brand-name">Broken Spur Rigs</span>
    </div>
    <ul class="address">
      <li>48310 E Calloway Ridge Rd S</li>
      <li>STE 217</li>
      <li>Marsh Hollow, CO 80219</li>
    </ul>
    <ul class="contact-lines">
      <li class="phone">720-555-0184
        <svg viewBox="0 0 24 24" aria-hidden="true"><path fill="#f26522" d="M6.6 10.8a15 15 0 0 0 6.6 6.6l2.2-2.2a1 1 0 0 1 1-.25 11.4 11.4 0 0 0 3.6.57 1 1 0 0 1 1 1V20a1 1 0 0 1-1 1A17 17 0 0 1 3 4a1 1 0 0 1 1-1h3.5a1 1 0 0 1 1 1c0 1.25.2 2.45.57 3.57a1 1 0 0 1-.25 1z"/></svg>
      </li>
      <li>dale@brokenspurrigs.example
        <svg viewBox="0 0 24 24" aria-hidden="true"><rect x="2" y="5" width="20" height="14" fill="#f26522"/><path d="M2 5l10 8 10-8" fill="none" stroke="#f4f4f3" stroke-width="1.6"/></svg>
      </li>
      <li>www.brokenspurrigs.example
        <svg viewBox="0 0 24 24" aria-hidden="true"><g fill="none" stroke="#f26522" stroke-width="2"><circle cx="12" cy="12" r="9.5"/><ellipse cx="12" cy="12" rx="4" ry="9.5"/><path d="M2.5 12h19M4 7h16M4 17h16"/></g></svg>
      </li>
    </ul>
  </section>

  <section class="card card--back">
    <span class="back-circle"></span>
    <p class="back-name">Broken Spur Rigs</p>
  </section>

</body>
</html>
```